Book Cover for the book: Walk the Path Laid Before You

We are wanting a rebranding of the book cover for the book - Walk the Path Laid Before You: How to Hear Your Inner Compass and Uncover Your Calling, Talents and Strength.

We would like to see front, back and spine designs included.

Please stay with the color schemes included in the existing cover (see attached) . We would like to see designs with a snowflake, or hummingbird element included in the design.

Back Cover should include the copy included in the attached file, incorporate all or some of the reviews included in the documents uploaded and image of author.

Please include the authors name: Marisol Pennwright on front, spine and back cover of the book

Target Market(s)

Healers, Visionaries

Requirements
Must have
• See Project Description

```html
<!DOCTYPE html>
<html lang="en">
<head>
<meta charset="utf-8">
<title>Walk the Path Laid Before You — Marisol Pennwright</title>
<link href="https://fonts.googleapis.com/css2?family=Cormorant+Garamond:wght@400;500&display=swap" rel="stylesheet">
<style>
  :root {
    --page: #ffffff;
    --sky-center: #a2effd;
    --sky-edge: #77d3f8;
    --title-plum: #9a4b99;
    --ink: #262626;
    --bird-blue: #3f8fc4;
    --bird-teal: #4fb7b0;
    --bird-gold: #e9b454;
  }
  * { margin: 0; padding: 0; box-sizing: border-box; }
  html, body {
    width: 1200px;
    height: 1200px;
    overflow: hidden;
    background: var(--page);
  }
  .book-cover {
    position: absolute;
    left: 276px;
    top: 99px;
    width: 648px;
    height: 1000px;
    background: radial-gradient(ellipse 60% 45% at 50% 52%, var(--sky-center) 0%, var(--sky-edge) 100%);
    overflow: hidden;
  }
  .subtitle {
    position: absolute;
    top: 58px;
    left: 0;
    right: 0;
    text-align: center;
    font-family: "Cormorant Garamond", Georgia, serif;
    font-weight: 500;
    font-size: 29px;
    line-height: 34px;
    color: var(--ink);
  }
  .title {
    position: absolute;
    top: 214px;
    left: 0;
    right: 0;
    height: 640px;
    display: flex;
    flex-direction: column;
    justify-content: space-between;
    align-items: center;
    font-family: "Cormorant Garamond", Georgia, serif;
    font-weight: 400;
    font-size: 104px;
    line-height: 1;
    letter-spacing: 0.2em;
    color: var(--title-plum);
  }
  .title span { display: block; margin-right: -0.2em; }
  .hummingbird {
    position: absolute;
    left: 211px;
    top: 522px;
    width: 212px;
    height: 286px;
    border-radius: 55% 45% 50% 50% / 40% 40% 60% 60%;
    background: radial-gradient(ellipse at 55% 35%, var(--bird-teal) 0%, var(--bird-blue) 40%, var(--bird-gold) 62%, rgba(63,143,196,0.35) 80%, rgba(63,143,196,0) 100%);
    opacity: 0.85;
  }
  .author {
    position: absolute;
    top: 905px;
    left: 0;
    right: 0;
    text-align: center;
    font-family: "Cormorant Garamond", Georgia, serif;
    font-weight: 500;
    font-size: 31px;
    letter-spacing: 0.3em;
    color: var(--ink);
  }
</style>
</head>
<body>
  <main class="book-cover">
    <p class="subtitle">How to Hear Your Inner Compass and<br>Uncover Your Calling, Talents<br>and Strength.</p>
    <h1 class="title">
      <span>WALK</span>
      <span>THE</span>
      <span>PATH</span>
      <span>LAID</span>
      <span>BEFORE</span>
      <span>YOU</span>
    </h1>
    <div class="hummingbird" role="img" aria-label="Watercolour hummingbird in blue, green and gold hovering across the title with long trailing tail feathers"></div>
    <p class="author">Marisol Pennwright</p>
  </main>
</body>
</html>
```